Tarno Booking website (www.tarnobooking.example)

My company develops booking software, Tarno Booking, for the hourly booking of resources such as classes in a school or customer booking involving rooms in a spa. These bookings also involve the customers, staff, rooms and a lesson or treatment.

The main difference between this software and general calendar software such as Plexo calendar is that this Tarno Booking allows resources such as people and rooms to be associated with the bookings. This is important for example in the case of a Spa to make sure the rooms are booked appropriately and to see the free times for the rooms. For a golf practice range the players much be booked to the tee spots where they practice golf.

I have tried to design the website myself, as a computer programmer- I am a bit "square" and not a designer, my first attempt is http://www.tarnobooking.example/, my second attempt is at http://www.quenbel-works.example/tarnobookingwebsite/
I am not happy with my designs as compared to the professional designs I see people can come up with here. The software must have the image of a professional software product in order to inspire the confidence of customers.

Am looking for a design which will be the most likely to give the customer the following feeling:
* Confident the product can do the job.
* Feel easy to want to try it, at least for the free trial.
* Its a professional software product and also a web based product, the user can login from the web.

Look at other booking software websites for ideas, here is a list of links to similar booking products. These products all have different features but are mostly for resource booking.
http://quenbel-works.example/tarnobookingwebsite/?page=compare

Hello all,

Thankyou for the designs so far, to save peoples time, I will try to eliminate the bottom 50% of designs now.

To be honest, most of the designs are of a good or high quality, I think its very tough on you as graphic and web designers. Only a minor few are of low quality.

If your design is discarded - I would say its unlikely that you are going to be able to produce a design that will beat the competition. 
You probably already know, you could try to re-sell your design later for other projects or as a template on one of those template websites. Some of these discarded designs are quite worthwhile designs.

Best regards, Dorian

Target Market(s)

Spa, Gym, School, Golf, any organization who manages bookings of their customers

Industry/Entity Type

Software

Requirements
Must have
• Home page and inner page, any other pages up to you.

Make a logo or use the image of the girl that I already have on the second design.

Menu(s) for navigation.

A language switcher for 3 languages, English, Chinese Traditional and Chinese Simplified. (Western, Hong Kong and Chinese mainland market are important).

Space for a video introduction, it could be small and when the user clicks on it then it gets bigger then it won't take up too much space. Up to you.

A space for the user to login and register a new account.

Screenshots.

I don't have any strong preferences, use your own ideas, if you look at all the other products you can get the basic idea from them.

The total goal is to make a website which is going to lead to sales of the software product.

```html
<!DOCTYPE html>
<html lang="en">
<head>
<meta charset="utf-8">
<title>Tarno Booking – Booking systems</title>
<link rel="stylesheet" href="https://fonts.googleapis.com/css2?family=Arimo:wght@400;700&family=Marcellus&family=Noto+Sans:wght@400;700&family=Oswald:wght@500&family=PT+Sans:wght@400;700&display=swap">
<style>
  :root{
    --sky:#3a70e8;
    --page:#c2c6d0;
    --white:#ffffff;
    --yellow:#ffec00;
    --ink:#1a1a1a;
    --muted:#555a63;
    --title-blue:#3a70e8;
    --navy:#1f3fa8;
    --orange:#f7941d;
    --tab-top:#eef0f8;
    --tab-bottom:#c6cde6;
    --band-top:#e2e5ee;
    --band-bottom:#d3d7e0;
    --footer:#161616;
    --green:#5cc62e;
    --video:#6b6f78;
  }
  *{box-sizing:border-box;margin:0;padding:0}
  html,body{width:1200px;height:1173px;overflow:hidden}
  body{position:relative;background:var(--page);font-family:"Noto Sans",sans-serif;color:var(--ink)}
  .abs{position:absolute}

  .sky{left:0;top:0;width:1200px;height:337px;background:var(--sky)}

  .utility{left:59px;top:27px;width:1082px;height:39px;
    background:linear-gradient(#f4f5fa,#c9cfe3);display:flex;align-items:center;justify-content:flex-end;
    padding-right:20px;gap:30px;font-family:"Marcellus",serif;font-size:17px;color:var(--ink)}
  .utility a{display:flex;align-items:center;gap:6px;color:inherit;text-decoration:none}
  .lang{width:137px;height:21px;border:1px solid #d8d100;background:var(--white);
    font-family:"Arimo",sans-serif;font-size:11px;display:flex;align-items:center;justify-content:space-between;padding:0 5px}

  .brand{left:72px;top:132px;width:300px}
  .brand-name{font-family:"PT Sans",sans-serif;font-weight:700;font-size:50px;color:var(--yellow);line-height:1;letter-spacing:-1px}
  .brand-rule{height:1px;background:#c8d6ff;margin:10px 0 6px 8px;width:292px}
  .brand-tag{font-family:"Marcellus",serif;color:#dbe4ff;font-size:19px;padding-left:40px}

  .video{left:484px;top:105px;width:657px;height:172px;background:var(--video);border:1px solid #e8e8e8;
    display:flex;align-items:center;justify-content:center;gap:12px;color:var(--white);
    font-family:"Arimo",sans-serif;font-size:20px;letter-spacing:1px}

  .sheet{left:49px;top:304px;width:1092px;height:748px;background:var(--white)}

  .nav{left:49px;top:331px;width:1092px;height:39px}
  .nav a{position:absolute;top:0;height:39px;background:linear-gradient(var(--tab-top),var(--tab-bottom));
    font-family:"Arimo",sans-serif;font-size:20px;color:var(--ink);text-decoration:none;
    display:flex;align-items:center;justify-content:center}

  .welcome{left:102px;top:407px;width:670px}
  .welcome h1{font-family:"PT Sans",sans-serif;font-weight:400;font-size:23px;color:var(--title-blue);margin-bottom:6px}
  .welcome p{font-size:15.4px;line-height:20.5px;margin-bottom:20px;letter-spacing:-.1px}

  .login{left:799px;top:395px;width:324px;height:292px;border-radius:8px;
    background:linear-gradient(#f2f2f2,#d6d6d6);padding:30px 20px}
  .login h2{font-family:"Oswald",sans-serif;font-weight:500;font-size:21px;color:#222;margin-bottom:14px;letter-spacing:-.3px}
  .login label{display:block;font-family:"Arimo",sans-serif;font-size:13.5px;color:#333;margin-bottom:4px}
  .field{width:266px;height:37px;background:var(--white);border-radius:7px;border:1px solid #e3e3e3;margin-bottom:14px}
  .login-row{display:flex;justify-content:space-between;align-items:center;margin-top:20px}
  .login-btn{font-family:"Oswald",sans-serif;font-size:20px;color:var(--white);text-shadow:0 0 1px #aaa}
  .signup{font-family:"Arimo",sans-serif;font-size:13.5px;color:#333;text-decoration:underline;margin-right:16px}

  .band{left:49px;top:710px;width:1092px;height:321px;background:linear-gradient(var(--band-top),var(--band-bottom))}

  .news{left:103px;top:738px;width:230px}
  .news h3{font-family:"Arimo",sans-serif;font-weight:700;font-size:22px;color:var(--title-blue);display:flex;align-items:center;gap:8px;margin-bottom:22px}
  .news-art{width:50px;height:50px;border-radius:6px;background:linear-gradient(#f7b24a,#9cc54b)}
  .news-item{font-family:"Arimo",sans-serif;font-weight:700;font-size:12px;color:#444;line-height:15px;margin-bottom:14px}
  .divider{left:343px;top:736px;width:2px;height:258px;background:var(--navy)}

  .fit{left:352px;top:721px;width:530px;height:288px;background:var(--white);border:1px solid #555;padding:12px 18px}
  .fit h3{font-family:"Arimo",sans-serif;font-weight:700;font-size:23px;color:var(--orange);display:inline-block;border-bottom:1px solid #bbb;margin-bottom:6px}
  .fit p{font-family:"Arimo",sans-serif;font-size:14px;color:#333;margin-bottom:10px}
  .fit ul{list-style:none;font-family:"Arimo",sans-serif;font-size:14px;color:#333;line-height:18px}
  .fit li{position:relative;padding-left:18px;margin-bottom:4px}
  .fit li::before{content:"";position:absolute;left:2px;top:5px;border-left:6px solid #333;border-top:4px solid transparent;border-bottom:4px solid transparent}
  .more{position:absolute;left:105px;bottom:12px;font-family:"Arimo",sans-serif;font-weight:700;font-size:15px;color:var(--navy);display:flex;align-items:center;gap:4px}

  .office{left:891px;top:722px;width:229px;height:284px;background:var(--white);padding:14px 15px}
  .office-art{width:50px;height:62px;margin:0 0 10px 62px;border-radius:8px;background:linear-gradient(#d9b08a,#3d8fd1)}
  .office h3{font-family:"PT Sans",sans-serif;font-weight:400;font-size:23px;color:var(--navy);margin-bottom:16px}
  .office p{font-family:"PT Sans",sans-serif;font-size:15px;color:var(--navy);line-height:18px;letter-spacing:.4px}
  .office .tel{margin-top:18px}

  .footer{left:0;top:1052px;width:1200px;height:108px;background:var(--footer)}
  .foot-nav{left:0;top:1094px;width:1200px;display:flex;justify-content:center;font-family:"Arimo",sans-serif;font-size:15.5px;padding-right:40px}
  .foot-nav a{color:var(--white);text-decoration:none;padding:0 10px;border-left:1px solid #555}
  .foot-nav a:first-child{border-left:none;color:var(--green)}
  .social{left:979px;top:1091px;display:flex;gap:4px}
  .social span{width:37px;height:37px;border-radius:5px;background:linear-gradient(#e4e4e4,#8a8a8a)}
</style>
</head>
<body>
  <div class="abs sky"></div>

  <div class="abs utility">
    <a href="#"><svg width="22" height="18" viewBox="0 0 22 18"><path d="M1 2h4l3 10h10l2-7H7" fill="none" stroke="#1f3fa8" stroke-width="2"/><circle cx="9" cy="15.5" r="1.8" fill="#1f3fa8"/><circle cx="17" cy="15.5" r="1.8" fill="#1f3fa8"/></svg>Shopping Cart</a>
    <a href="#"><svg width="20" height="14" viewBox="0 0 20 14"><rect x="1" y="1" width="18" height="12" fill="#1f3fa8"/><path d="M1 1l9 7 9-7" fill="none" stroke="#fff" stroke-width="1.4"/></svg>Contact Us</a>
    <a href="#"><svg width="18" height="15" viewBox="0 0 18 15"><rect x="1" y="1" width="16" height="13" fill="#1f3fa8"/><path d="M4 4l10 7M14 4L4 11" stroke="#fff" stroke-width="1.4"/></svg>About Us</a>
    <div class="lang">Select Language <svg width="12" height="12" viewBox="0 0 12 12"><circle cx="6" cy="6" r="5" fill="none" stroke="#333"/><path d="M3.5 5l2.5 3 2.5-3z" fill="#333"/></svg></div>
  </div>

  <div class="abs brand">
    <div class="brand-name">Tarno Booking</div>
    <div class="brand-rule"></div>
    <div class="brand-tag">Booking systems</div>
  </div>

  <div class="abs video">
    <svg width="44" height="44" viewBox="0 0 44 44"><circle cx="22" cy="22" r="19.5" fill="none" stroke="#fff" stroke-width="2.5"/><path d="M16 11l15 11-15 11 5-11z" fill="#fff"/></svg>
    PLAY
  </div>

  <div class="abs sheet"></div>

  <nav class="abs nav">
    <a href="#" style="left:0;width:282px">About Tarno Booking</a>
    <a href="#" style="left:289px;width:122px">Videos</a>
    <a href="#" style="left:418px;width:184px">Documentation</a>
    <a href="#" style="left:609px;width:150px">Free Trial</a>
    <a href="#" style="left:766px;width:137px">Purchase</a>
    <a href="#" style="left:911px;width:181px">Compare</a>
  </nav>

  <section class="abs welcome">
    <h1>Welcome to TARNO BOOKING !</h1>
    <p>Tarno Booking is front office booking software which makes managing bookings, room and staff availability fast and simple. We focus on producing quality software which is powerful yet easy to use.</p>
    <p>This is suitable for many types of business, click here to view all the available business types and to learn more about how this software can help you directly.</p>
    <p>Tarno Booking stores all data on our servers in the SaaS model giving a very low total cost of ownership our customers. You have zero investment in server platform hardware, zero investment in software licenses, zero investment in hardware and software upgrades, as these are included as part of the service.</p>
  </section>

  <form class="abs login">
    <h2>USER LOGIN</h2>
    <label>Enter username:</label>
    <div class="field"></div>
    <label>Enter password:</label>
    <div class="field"></div>
    <div class="login-row">
      <span class="login-btn">LOGIN</span>
      <a class="signup" href="#">Don't have account yet?</a>
    </div>
  </form>

  <div class="abs band"></div>

  <section class="abs news">
    <h3>Latest News <span class="news-art" role="img" aria-label="News feed illustration"></span></h3>
    <div class="news-item">Friday 28th October, 2011<br>News title goes here</div>
    <div class="news-item">Friday 28th October, 2011<br>News title goes here</div>
    <div class="news-item">Friday 28th October, 2011<br>News title goes here</div>
    <div class="news-item">Friday 28th October, 2011<br>News title goes here</div>
  </section>
  <div class="abs divider"></div>

  <section class="abs fit">
    <h3>Is Tarno Booking suitable for my business?</h3>
    <p>Tarno Booking works well for the following types of businesses:</p>
    <ul>
      <li>Spa, Gym, Weight Management Center or Nail Salon</li>
      <li>Golf Practice range with many tees for golfers to practice golf</li>
      <li>Room bookings such as meeting rooms, library rooms, computer rooms</li>
      <li>Conference or meeting bookings</li>
      <li>Language teaching school, Music school, Educational center or General school</li>
      <li>School which consults to schools by sending teachers to those schools</li>
    </ul>
    <span class="more"><svg width="12" height="16" viewBox="0 0 12 16"><path d="M2 1l8 7-8 7" fill="none" stroke="#555" stroke-width="3"/></svg>More</span>
  </section>

  <section class="abs office">
    <div class="office-art" role="img" aria-label="Contact person icon"></div>
    <h3>Main Office</h3>
    <p>Larkfield Works<br>48 Ormond Lane<br>13th Floor<br>Westbury, NV 30417</p>
    <p class="tel">Tel:&nbsp;&nbsp;&nbsp; 555-014-8200<br>Fax:&nbsp;&nbsp;&nbsp; 555-014-8242</p>
  </section>

  <div class="abs footer"></div>
  <nav class="abs foot-nav">
    <a href="#">Home</a><a href="#">Company</a><a href="#">Services</a><a href="#">Solutions</a><a href="#">Partners</a><a href="#">Contacts</a>
  </nav>
  <div class="abs social"><span></span><span></span><span></span></div>
</body>
</html>
```